Create Vertical Dog Food Labels (3 inches x 5 inches) for PupKitchen

We need a packing Vertical label (3 inches x 5 inches) design for our line of Dog Food - Pup Kitchen at pupkitchenmeals.com (please review website). This design is for Custom Roll Labels. We have a logo already. Use our logo colors on label. What we need incorporated is a list of our ingredients:

50% Choice Beef
20% Pasture-raised Chicken
15% Brown Rice
15% Fresh Vegetables - Carrots, Kale, Zucchini
Herbal Health Boosters

We also need these lines at the bottom of the label:

Keeps in fridge for 4 days after thawing
Stores in freezer up to 6 months
Questions? email us at orders@meadowlanepantry.com

We have attached a sample of a competitor. The Kibble Crate.

Target Market(s)

Dog owners

Industry/Entity Type

Dog Food

Font styles to use
Sans Serif

Requirements
Must have
• Read project description above
Nice to have
• Our logo color incorporated
Should not have
• I want it simple.

```html
<!DOCTYPE html>
<html lang="en">
<head>
<meta charset="UTF-8">
<title>PupKitchen – Dog Food Label</title>
<link rel="stylesheet" href="https://fonts.googleapis.com/css2?family=Poppins:wght@400;500;600&family=Arimo:wght@400;700&display=swap">
<style>
  :root {
    --backdrop: #cbcbcb;
    --paper: #f3e9da;
    --paper-dark: #eadcc6;
    --frame: #f7a300;
    --rule: #f2683a;
    --green: #0b6b0b;
    --green-soft: #7fbd3f;
    --warning: #f2683a;
    --sketch: #f3b24a;
  }
  * { box-sizing: border-box; margin: 0; padding: 0; }
  html, body { width: 896px; height: 1200px; overflow: hidden; }
  body { background: var(--backdrop); position: relative; }

  .label {
    position: absolute;
    left: 148px; top: 99px;
    width: 600px; height: 1001px;
    background: radial-gradient(ellipse at 50% 40%, var(--paper) 0%, var(--paper-dark) 100%);
    color: var(--green);
    font-family: "Poppins", sans-serif;
  }
  .label__frame { position: absolute; left: 0; top: 0; width: 600px; height: 1001px; }

  .brand-dot {
    position: absolute; left: 210px; top: 55px;
    width: 180px; height: 180px; border-radius: 50%;
    background: var(--green-soft);
  }
  .brand-name {
    position: absolute; left: 0; right: 0; top: 238px;
    text-align: center;
    font-family: "Poppins", sans-serif;
    font-weight: 600; font-size: 52px; letter-spacing: 1px;
    color: var(--green);
  }

  .ingredients { position: absolute; left: 51px; top: 369px; width: 497px; }
  .ingredients__table { width: 100%; border-collapse: collapse; }
  .ingredients__table td {
    border-top: 1.5px solid var(--rule);
    border-bottom: 1.5px solid var(--rule);
    font-size: 21px; line-height: 24px; vertical-align: middle;
    padding: 0 14px;
  }
  .ingredients__table tr:first-child td { height: 43px; }
  .ingredients__table tr:last-child td { height: 62px; }
  .ingredients__table td:first-child { width: 249px; border-right: 1.5px solid var(--rule); }
  .ingredients__table td:last-child { padding-left: 52px; }
  .ingredients__extra { text-align: center; font-size: 21px; line-height: 23px; margin-top: 9px; }

  .dog-portraits {
    position: absolute; left: 51px; top: 577px; width: 496px; height: 186px;
    background: radial-gradient(ellipse at center, rgba(243,178,74,0.28) 0%, rgba(243,178,74,0.08) 70%, rgba(243,178,74,0) 100%);
  }

  .storage {
    position: absolute; left: 0; right: 0; top: 810px;
    text-align: center;
    font-family: "Arimo", sans-serif; font-size: 24px; line-height: 28px;
    color: var(--warning);
  }
  .contact {
    position: absolute; left: 0; right: 0; top: 892px;
    text-align: center;
    font-family: "Arimo", sans-serif; font-size: 24px; line-height: 30px;
    color: var(--green);
  }
  .contact__email { font-weight: 700; font-size: 22px; }
</style>
</head>
<body>
  <section class="label">
    <svg class="label__frame" viewBox="0 0 600 1001" aria-hidden="true">
      <path d="M49 19 H533 A30 30 0 0 0 563 49 V952 A30 30 0 0 0 533 982 H49 A30 30 0 0 0 19 952 V49 A30 30 0 0 0 49 19 Z"
            fill="none" stroke="#f7a300" stroke-width="2.5"/>
    </svg>

    <div class="brand-dot" aria-hidden="true"></div>
    <h1 class="brand-name">PupKitchen</h1>

    <div class="ingredients">
      <table class="ingredients__table">
        <tr><td>50% Choice Beef</td><td>15% Brown Rice</td></tr>
        <tr><td>20% Pasture-raised Chicken</td><td>Herbal Health Boosters</td></tr>
      </table>
      <p class="ingredients__extra">15% Fresh Vegetables - Carrots,<br>Kale, Zucchini</p>
    </div>

    <div class="dog-portraits" role="img" aria-label="Line sketch of three dog heads: a chihuahua, a French bulldog and a golden retriever"></div>

    <p class="storage">Keeps in fridge for 4 days after thawing<br>Stores in freezer up to 6 months</p>

    <p class="contact">Questions? email us at<br><span class="contact__email">orders@meadowlanepantry.com</span></p>
  </section>
</body>
</html>
```